Quillex Landing Page & Logo

We are building a landing page for a new blockchain-based project called Quillex. The site should look modern and minimalistic with a very brief description of the upcoming project ("Unlock your Brevitan governance stack. Win weekly prizes and a quarterly jackpot!"), a viper logo (the animal - but can just be lettering) , and a button to subscribe for updates and early access.
Examples of similar pages:
https://pondru.finance/
https://www.zentrimo.org/
https://lumbrecks.com/
https://q8.io/
https://www.tovern.finance/
Crypto Users (Specifically Brevitan holders)

```html
<!DOCTYPE html>
<html lang="en">
<head>
<meta charset="utf-8">
<title>Quillex Finance</title>
<link rel="stylesheet" href="https://fonts.googleapis.com/css2?family=Alfa+Slab+One&family=Playfair+Display:wght@400;700&family=Mulish:wght@400;600&display=swap">
<style>
:root{
  --navy:#020a1c;
  --navy-2:#061430;
  --ink:#0b0f1a;
  --red:#e8333b;
  --cyan:#21d4e6;
  --blue:#0a9be3;
  --grey:#e8e8e8;
  --light:#f2f2f2;
  --white:#ffffff;
  --text:#2b2b2b;
  --display:'Alfa Slab One', serif;
  --serif:'Playfair Display', serif;
  --sans:'Mulish', sans-serif;
}
*{box-sizing:border-box;margin:0;padding:0}
html,body{width:1200px;height:3195px;overflow:hidden}
body{position:relative;font-family:var(--sans);color:var(--text);background:var(--white)}
.abs{position:absolute}
section,header,footer{position:absolute;left:0;width:1200px;overflow:hidden}

/* Hero */
.hero{top:0;height:679px;background:linear-gradient(100deg,#0b3a66 0%,#0d3157 40%,#1b2c40 62%,#5a3a1c 85%,#8a5a22 100%)}
.hero-art{position:absolute;left:490px;top:40px;width:710px;height:639px;background:radial-gradient(ellipse at 55% 55%,rgba(255,170,60,.35),rgba(20,60,100,0) 65%)}
.brand{position:absolute;font-family:var(--serif);font-weight:700;color:var(--white);letter-spacing:1px}
.hero .brand{left:151px;top:18px;font-size:42px;line-height:1}
.tagline{position:absolute;font-family:var(--sans);font-size:11px;color:var(--white);letter-spacing:.2px}
.hero .tagline{left:130px;top:71px}
.nav{position:absolute;top:24px;left:559px;display:flex;gap:0;font-size:15px;color:var(--white)}
.nav a{color:inherit;text-decoration:none;margin-right:31px}
.nav a.active{color:var(--blue)}
.hero-title{position:absolute;left:131px;top:220px;font-family:var(--display);font-size:62px;color:var(--white);text-shadow:-3px 3px 0 var(--red);letter-spacing:1px}
.hero-copy{position:absolute;left:137px;top:320px;width:420px;font-family:var(--serif);font-size:20px;line-height:29px;color:var(--white)}
.btn-dark{position:absolute;left:137px;top:410px;width:134px;height:46px;border-radius:12px;background:#05070d;color:var(--white);font-family:var(--serif);font-weight:700;font-size:18px;display:flex;align-items:center;justify-content:center;box-shadow:3px 3px 0 var(--red)}

/* Section titles */
.section-title{position:absolute;left:0;width:1200px;text-align:center;font-family:var(--display);font-size:29px;letter-spacing:.5px}
.section-title.on-dark{color:var(--white);text-shadow:-2px 2px 0 var(--red)}
.section-title.on-light{color:var(--ink);text-shadow:-2px 2px 0 var(--red)}
.rule{position:absolute;width:34px;height:3px}

/* Solutions */
.solutions{top:679px;height:525px;background:var(--navy)}
.sol-col{position:absolute;top:172px;width:252px;text-align:center;color:var(--white)}
.sol-col svg{display:block;margin:0 auto}
.sol-col h3{font-family:var(--serif);font-weight:700;font-size:20px;margin-top:14px;margin-bottom:8px}
.sol-col p{font-size:14px;line-height:17.5px;padding:0 20px}
.divider{position:absolute;top:172px;width:1px;height:298px;background:rgba(255,255,255,.25)}

/* Why */
.why{top:1204px;height:665px;background:var(--grey)}
.why-intro{position:absolute;left:129px;top:131px;width:395px;font-size:14px;line-height:17.5px}
.feature{position:absolute;left:130px;width:400px;height:90px}
.feature .icon-box{position:absolute;left:7px;top:0;width:87px;height:80px;background:var(--ink);box-shadow:-7px 7px 0 var(--red);display:flex;align-items:center;justify-content:center}
.feature h4{position:absolute;left:117px;top:0;font-family:var(--serif);font-size:19px;font-weight:700;color:var(--ink)}
.feature p{position:absolute;left:117px;top:31px;width:270px;font-size:14px;line-height:17.5px}
.sphere{position:absolute;left:602px;top:136px;width:459px;height:453px;border-radius:50%;background:radial-gradient(circle at 45% 40%,#ffffff 0%,#dfeaf4 55%,#8fc8f0 80%,rgba(232,232,232,0) 100%)}

/* Fast & secure */
.fast{top:1869px;height:491px;background:var(--white)}
.fast-art{position:absolute;left:130px;top:42px;width:540px;height:410px;border-radius:30px;background:linear-gradient(160deg,#e6f6fb 0%,#bfe6f4 45%,#e9e4f4 100%)}
.fast h2{position:absolute;left:711px;top:76px;font-family:var(--display);font-size:29px;color:var(--ink);text-shadow:-2px 2px 0 var(--red)}
.fast-copy{position:absolute;left:714px;top:165px;width:356px;font-size:13.5px;line-height:21px}
.btn-blue{position:absolute;left:717px;top:2231px;width:114px;height:40px;border-radius:10px;background:var(--blue);color:var(--white);font-family:var(--serif);font-weight:700;font-size:15px;display:flex;align-items:center;justify-content:center}

/* Upcoming */
.upcoming{top:2360px;height:522px;background:var(--light)}
.card{position:absolute;top:113px;width:289px}
.card.featured{background:var(--white);height:376px;box-shadow:0 4px 16px rgba(0,0,0,.12);border-radius:6px}
.card .thumb{height:196px;border-radius:6px}
.card h5{font-family:var(--serif);font-size:15px;font-weight:400;line-height:19px;color:var(--ink);margin:21px 0 14px;padding-right:10px}
.card p{font-size:12.5px;line-height:15.5px;padding-right:14px}
.card.featured h5,.card.featured p{padding-left:23px}
.btn-pill{display:inline-flex;margin:18px 0 0 22px;width:96px;height:30px;border-radius:15px;background:var(--blue);color:var(--white);font-family:var(--serif);font-size:13px;align-items:center;justify-content:center}

/* Footer */
.site-footer{top:2882px;height:313px;background:var(--navy)}
.site-footer .brand{left:183px;top:63px;font-size:42px;line-height:1}
.site-footer .tagline{left:160px;top:110px}
.follow{position:absolute;left:243px;top:154px;font-size:14px;color:var(--white)}
.socials{position:absolute;left:213px;top:190px;display:flex;gap:15px}
.socials span{width:30px;height:30px;border-radius:3px}
.sub-title{position:absolute;left:556px;top:43px;font-family:var(--display);font-size:20px;color:var(--white);text-shadow:-2px 2px 0 var(--red)}
.email{position:absolute;left:558px;top:89px;width:350px;height:41px;background:var(--white);border:1px solid #ccc;font-size:13px;color:#555;padding:13px 14px}
.btn-sub{position:absolute;left:921px;top:89px;width:151px;height:41px;background:var(--blue);color:var(--white);font-family:var(--display);font-size:20px;display:flex;align-items:center;justify-content:center}
.foot-nav{position:absolute;left:556px;top:183px;display:flex;font-size:14.5px;color:var(--white)}
.foot-nav a{color:inherit;text-decoration:none;margin-right:31px}
.foot-line{position:absolute;left:556px;top:233px;width:512px;height:1px;background:rgba(255,255,255,.35)}
.copyright{position:absolute;right:130px;top:263px;font-size:12.5px;color:var(--white)}
</style>
</head>
<body>

<header class="hero">
  <div class="hero-art" role="img" aria-label="Illustration of a coin in a glass bulb over a glowing circuit platform"></div>
  <div class="brand">QUILLEX</div>
  <div class="tagline">UNLOCK YOUR GOVERANCE BREVs. WIN BIG.</div>
  <nav class="nav">
    <a class="active">Home</a><a>About Us</a><a>White Paper</a><a>Project</a><a>News</a><a>Contact us</a>
  </nav>
  <h1 class="hero-title">QUILLEX FINANCE</h1>
  <p class="hero-copy">Lorem Ipsum is simply dummy text of the printing and typesetting industry</p>
  <div class="btn-dark">Read More</div>
</header>

<section class="solutions">
  <h2 class="section-title on-dark" style="top:44px">SOLUTIONS</h2>
  <div class="rule" style="left:583px;top:104px;background:var(--white)"></div>

  <div class="sol-col" style="left:89px">
    <svg width="70" height="70" viewBox="0 0 70 70" fill="none" stroke-width="4" stroke-linecap="round">
      <g transform="translate(3,3)" stroke="var(--red)"><path d="M18 40h34a11 11 0 0 0 0-22 16 16 0 0 0-30-2 12 12 0 0 0-4 24z"/><path d="M24 40v10M35 40v14M46 40v10"/><circle cx="24" cy="53" r="3"/><circle cx="35" cy="58" r="3"/><circle cx="46" cy="53" r="3"/></g>
      <g stroke="var(--white)"><path d="M18 40h34a11 11 0 0 0 0-22 16 16 0 0 0-30-2 12 12 0 0 0-4 24z"/><path d="M24 40v10M35 40v14M46 40v10"/><circle cx="24" cy="53" r="3"/><circle cx="35" cy="58" r="3"/><circle cx="46" cy="53" r="3"/></g>
    </svg>
    <h3>Unbiased Code</h3>
    <p>There are many variations of passages of Lorem Ipsum available, but the majority have suffered alteration in some form, by injected humour,</p>
  </div>
  <div class="divider" style="left:334px"></div>

  <div class="sol-col" style="left:330px;top:162px">
    <svg width="70" height="70" viewBox="0 0 70 70" fill="none" stroke-width="4" stroke-linejoin="round">
      <g transform="translate(3,3)" stroke="var(--red)"><path d="M14 8h42v54H44V50H26v12H14z"/><circle cx="35" cy="28" r="8"/></g>
      <g stroke="var(--white)"><path d="M14 8h42v54H44V50H26v12H14z"/><circle cx="35" cy="28" r="8"/></g>
    </svg>
    <h3>Safe and Secure</h3>
    <p>There are many variations of passages of Lorem Ipsum available, but the majority have suffered alteration in some form, by injected humour,</p>
  </div>
  <div class="divider" style="left:586px"></div>

  <div class="sol-col" style="left:584px;top:162px">
    <svg width="70" height="70" viewBox="0 0 70 70" fill="none" stroke-width="4">
      <g transform="translate(2,2)" stroke="var(--red)"><circle cx="35" cy="20" r="15"/><path d="M35 35v10M12 50h46"/><rect x="8" y="52" width="14" height="8" rx="4"/><rect x="28" y="52" width="14" height="8" rx="4"/><rect x="48" y="52" width="14" height="8" rx="4"/></g>
      <g stroke="var(--white)"><circle cx="35" cy="20" r="15"/><path d="M35 35v10M12 50h46"/><rect x="8" y="52" width="14" height="8" rx="4"/><rect x="28" y="52" width="14" height="8" rx="4"/><rect x="48" y="52" width="14" height="8" rx="4"/></g>
      <text x="35" y="28" text-anchor="middle" font-family="Mulish,sans-serif" font-weight="600" font-size="20" fill="var(--white)" stroke="none">$</text>
    </svg>
    <h3>Stable Value</h3>
    <p>There are many variations of passages of Lorem Ipsum available, but the majority have suffered alteration in some form, by injected humour,</p>
  </div>
  <div class="divider" style="left:843px"></div>

  <div class="sol-col" style="left:850px;top:162px">
    <svg width="70" height="70" viewBox="0 0 70 70" fill="none" stroke-width="4">
      <g transform="translate(3,3)" stroke="var(--red)"><circle cx="33" cy="35" r="25"/><ellipse cx="33" cy="35" rx="11" ry="25"/><path d="M8 35h50M12 22h42M12 48h42"/></g>
      <g stroke="var(--white)"><circle cx="33" cy="35" r="25"/><ellipse cx="33" cy="35" rx="11" ry="25"/><path d="M8 35h50M12 22h42M12 48h42"/></g>
    </svg>
    <h3>Borderless Economy</h3>
    <p>There are many variations of passages of Lorem Ipsum available, but the majority have suffered alteration in some form, by injected humour,</p>
  </div>
</section>

<section class="why">
  <h2 class="section-title on-light" style="top:38px">WHY QUILLEX</h2>
  <div class="rule" style="left:583px;top:86px;background:var(--ink)"></div>
  <p class="why-intro">Sed ut perspiciatis unde omnis iste natus error sit voluptatem accusantium doloremque laudantium, totam rem aperiam, eaque ipsa quae ab illo inventore veritatis et quasi architecto beatae vitae dicta sunt explicabo. Nemo enim ipsam voluptatem quia voluptas sit aspernatur.</p>

  <div class="feature" style="top:263px">
    <div class="icon-box"><svg width="46" height="50" viewBox="0 0 46 50" fill="none" stroke="var(--cyan)" stroke-width="3"><path d="M23 3l18 7v14c0 12-8 20-18 23C13 44 5 36 5 24V10z"/><rect x="16" y="23" width="14" height="11" fill="var(--cyan)"/><path d="M18 23v-4a5 5 0 0 1 10 0v4"/></svg></div>
    <h4>Store of Value</h4>
    <p>There are many variations of passages of Lorem Ipsum available, but the majority have suffered alteration.</p>
  </div>
  <div class="feature" style="top:385px">
    <div class="icon-box"><svg width="56" height="56" viewBox="0 0 56 56" fill="none" stroke="var(--cyan)" stroke-width="2.5"><circle cx="28" cy="28" r="9"/><circle cx="28" cy="25" r="3"/><path d="M22 34a6 6 0 0 1 12 0"/><path d="M28 19V9M28 37v10M19 28H9M37 28h10M21 21l-7-7M35 35l7 7M35 21l7-7M21 35l-7 7"/><circle cx="28" cy="6" r="3"/><circle cx="28" cy="50" r="3"/><circle cx="6" cy="28" r="3"/><circle cx="50" cy="28" r="3"/><circle cx="12" cy="12" r="3"/><circle cx="44" cy="44" r="3"/><circle cx="44" cy="12" r="3"/><circle cx="12" cy="44" r="3"/></svg></div>
    <h4>Decentralized</h4>
    <p>There are many variations of passages of Lorem Ipsum available, but the majority have suffered alteration.</p>
  </div>
  <div class="feature" style="top:516px">
    <div class="icon-box"><svg width="56" height="50" viewBox="0 0 56 50" fill="none" stroke="var(--cyan)" stroke-width="2.5"><ellipse cx="28" cy="6" rx="7" ry="3"/><path d="M21 6v10c0 2 14 2 14 0V6"/><path d="M28 18v8M8 26h40M8 26v8M28 26v8M48 26v8"/><rect x="3" y="34" width="10" height="12"/><rect x="23" y="34" width="10" height="12"/><rect x="43" y="34" width="10" height="12"/></svg></div>
    <h4>Superior Infrastructure</h4>
    <p>There are many variations of passages of Lorem Ipsum available, but the majority have suffered alteration.</p>
  </div>

  <div class="sphere" role="img" aria-label="Illustration of a white geodesic network sphere with blue nodes"></div>
</section>

<section class="fast">
  <div class="fast-art" role="img" aria-label="Isometric illustration of a blockchain platform linked to mining, smart contract, market and coin blocks"></div>
  <h2>FAST &amp; SECURE</h2>
  <div class="rule" style="left:714px;top:122px;background:var(--ink)"></div>
  <p class="fast-copy">Sed ut perspiciatis unde omnis iste natus error sit voluptatem accusantium doloremque laudantium, totam rem aperiam, eaque ipsa quae ab illo inventore veritatis et quasi architecto beatae vitae dicta sunt explicabo. Nemo enim ipsam voluptatem quia voluptas sit aspernatur. eius modi tempora incidunt ut labore et dolore magnam aliquam quaerat voluptatem. Ut enim ad minima veniam, quis nostrum</p>
</section>
<div class="btn-blue">Read More</div>

<section class="upcoming">
  <h2 class="section-title on-light" style="top:32px">UPCOMING PROJECT</h2>
  <div class="rule" style="left:583px;top:81px;background:var(--ink)"></div>

  <article class="card" style="left:132px">
    <div class="thumb" role="img" aria-label="Illustration of glowing isometric server blocks on a dark blue field" style="background:radial-gradient(circle at 55% 45%,#1f7a9a,#0d3d8a 55%,#0a2a6e)"></div>
    <h5>Lorem ipsum dolor sit amet, consecte adipiscing elit, sed do eiusmod</h5>
    <p>Sed ut perspiciatis unde omnis iste natus error sit voluptatem accusantium doloremque laudantium, totam rem aperiam.</p>
  </article>

  <article class="card featured" style="left:456px">
    <div class="thumb" role="img" aria-label="Illustration of a laptop, wallet and coins on a purple field" style="background:linear-gradient(135deg,#8a6fc4,#5a3f9e 60%,#3d2a7a);border-radius:6px 6px 0 0"></div>
    <h5>Lorem ipsum dolor sit amet, consecte adipiscing elit, sed do eiusmod</h5>
    <p>Sed ut perspiciatis unde omnis iste natus error sit voluptatem accusantium doloremque laudantium.</p>
    <span class="btn-pill">View prizes</span>
  </article>

  <article class="card" style="left:780px">
    <div class="thumb" role="img" aria-label="Illustration of an isometric lab machine with glowing parts on a violet field" style="background:radial-gradient(circle at 50% 45%,#7b3fd0,#4a1fa0 60%,#34137a)"></div>
    <h5>Lorem ipsum dolor sit amet, consecte adipiscing elit, sed do eiusmod</h5>
    <p>Sed ut perspiciatis unde omnis iste natus error sit voluptatem accusantium doloremque laudantium, totam rem aperiam.</p>
  </article>
</section>

<footer class="site-footer">
  <div class="brand">QUILLEX</div>
  <div class="tagline">UNLOCK YOUR GOVERANCE BREVs. WIN BIG.</div>
  <div class="follow">Follow us</div>
  <div class="socials" aria-label="Social links">
    <span style="background:#3b5aa0"></span>
    <span style="background:#2a9ee0"></span>
    <span style="background:#d6287a"></span>
  </div>
  <h3 class="sub-title">SUBSCRIBE FOR UPDATES</h3>
  <div class="email">E mail id</div>
  <div class="btn-sub">SUBSCRIBE</div>
  <nav class="foot-nav"><a>Home</a><a>About Us</a><a>White Paper</a><a>Project</a><a>News</a><a>Contact us</a></nav>
  <div class="foot-line"></div>
  <div class="copyright">Copyright © 2022 All Rights Reserved</div>
</footer>

</body>
</html>
```